Quiet Harbor, Weekly therapy lessons for the heart of a sister missionary

This is a weekly guided therapy book for female Mormon missionaries. They leave for their missions for 18 months and I am a psychotherapist that is creating a guided workbook to help them through mental health struggles on their mission. I need a good book cover, also preferably something for the spine and back as well. I would like something that gives a soft and safe feeling.

```html
<!DOCTYPE html>
<html lang="en">
<head>
<meta charset="utf-8">
<title>Quiet Harbor — Book Cover</title>
<link rel="stylesheet" href="https://fonts.googleapis.com/css2?family=Crimson+Pro:wght@400;600&display=swap">
<style>
  :root {
    --page-bg: #efe9e1;
    --sky-top: #b7c2df;
    --sky-lilac: #d9d2e6;
    --cloud-pink: #f1d5d2;
    --glow: #fff4e2;
    --sun: #fbd9a0;
    --mountain: #c7a6b4;
    --meadow: #a7b784;
    --meadow-deep: #8da16e;
    --path: #efe2cf;
    --title-gold: #a47a34;
    --rule-gold: #b88f45;
    --subtitle: #5f5a5c;
    --author: #2f2b2c;
  }
  * { margin: 0; padding: 0; box-sizing: border-box; }
  html, body {
    width: 1200px;
    height: 730px;
    overflow: hidden;
    background: var(--page-bg);
  }
  .stage {
    width: 1200px;
    height: 730px;
    display: flex;
    align-items: center;
    justify-content: center;
  }
  .book-cover {
    position: relative;
    width: 454px;
    height: 680px;
    overflow: hidden;
    box-shadow: 0 6px 18px rgba(60, 45, 30, 0.18);
  }
  .cover-art {
    position: absolute;
    inset: 0;
    background: linear-gradient(180deg,
      var(--sky-top) 0%,
      var(--sky-lilac) 16%,
      var(--cloud-pink) 34%,
      var(--glow) 52%,
      var(--sun) 63%,
      var(--mountain) 69%,
      var(--meadow) 78%,
      var(--meadow-deep) 88%,
      var(--path) 100%);
  }
  .cover-text {
    position: relative;
    height: 100%;
    text-align: center;
    font-family: "Crimson Pro", Georgia, serif;
  }
  .title {
    padding-top: 112px;
    font-weight: 600;
    font-size: 64px;
    line-height: 1;
    color: var(--title-gold);
    letter-spacing: -0.5px;
  }
  .title-rule {
    display: block;
    width: 360px;
    height: 20px;
    margin: 2px auto 0;
  }
  .subtitle {
    margin-top: 14px;
    font-weight: 400;
    font-size: 22px;
    line-height: 1.2;
    color: var(--subtitle);
  }
  .author {
    position: absolute;
    left: 0;
    right: 0;
    bottom: 44px;
    font-weight: 400;
    font-size: 25px;
    letter-spacing: 4px;
    color: var(--author);
  }
</style>
</head>
<body>
  <main class="stage">
    <section class="book-cover">
      <div class="cover-art" role="img" aria-label="Soft painted landscape: pastel sunrise sky with pink clouds, sun rising between mauve mountains, and a path winding through a meadow of pink and white flowers"></div>
      <div class="cover-text">
        <h1 class="title">Quiet Harbor</h1>
        <svg class="title-rule" viewBox="0 0 360 20" aria-hidden="true">
          <path d="M2 14 C 90 4, 250 2, 358 10 C 250 6, 90 8, 2 14 Z" fill="var(--rule-gold)"/>
        </svg>
        <p class="subtitle">Weekly therapy lessons for<br>the heart of a sister missionary</p>
        <p class="author">AUTHOR NAME</p>
      </div>
    </section>
  </main>
</body>
</html>
```